K&R Security Services PTY. LTD.

Ive just had my logo made and I'm looking for some simple but strong designs for my business cards the company is a security company.

Please use dark colors.

Regards,

Owen Calder

Reason: Need more time for discussion with other directors

Industry/Entity Type

Security

Font styles to use
Sans Serif
Decorative

```html
<!DOCTYPE html>
<html lang="en">
<head>
<meta charset="utf-8">
<title>K&amp;R Security Services – Business Card</title>
<link rel="stylesheet" href="https://fonts.googleapis.com/css2?family=Open+Sans:wght@400;600;700&display=swap">
<style>
  :root {
    --page: #e9e7e4;
    --card-grey: #8f8f8f;
    --grey-light: #a8a8a8;
    --grey-mid: #7a7a7a;
    --grey-deep: #5c5c5c;
    --band-dark: #2a2a2a;
    --text-light: #e6e6e6;
    --text-muted: #a9a9a9;
    --name-grey: #bdbdbd;
  }
  * { margin: 0; padding: 0; box-sizing: border-box; }
  html, body { width: 1200px; height: 1000px; overflow: hidden; }
  body {
    background: var(--page);
    font-family: "Open Sans", Arial, sans-serif;
    position: relative;
  }
  .card {
    position: absolute;
    left: 250px;
    width: 700px;
    height: 400px;
    overflow: hidden;
    box-shadow: 0 6px 18px rgba(0,0,0,0.25);
  }
  .card--front { top: 70px; }
  .card--back { top: 530px; }
  .card svg.card__art { position: absolute; inset: 0; }
  .wordmark {
    position: absolute;
    display: flex;
    align-items: center;
    gap: 12px;
    color: #ffffff;
    font-weight: 700;
    letter-spacing: 2px;
  }
  .wordmark__dot {
    width: 22px; height: 22px;
    border-radius: 50%;
    background: var(--band-dark);
  }
  .card--front .wordmark {
    left: 0; right: 0; top: 170px;
    justify-content: center;
    font-size: 54px;
  }
  .card--back .wordmark {
    left: 48px; top: 70px;
    font-size: 34px;
  }
  .card--back .wordmark__dot { width: 16px; height: 16px; }
  .person {
    position: absolute;
    left: 48px; top: 262px;
  }
  .person__name {
    font-size: 26px; font-weight: 700;
    color: var(--name-grey); letter-spacing: 0.5px;
    text-transform: uppercase;
  }
  .person__title {
    font-size: 16px; color: var(--text-muted);
    letter-spacing: 2px; margin-top: -2px;
  }
  .contact {
    position: absolute;
    left: 390px; top: 172px;
    color: var(--text-light);
    font-size: 16px; line-height: 23px;
  }
  .contact__company { font-weight: 700; font-size: 16px; }
  .contact__address { padding-left: 10px; }
  .contact__row { display: flex; align-items: center; gap: 10px; padding-left: 10px; }
  .contact__icon { width: 14px; height: 14px; flex: none; }
</style>
</head>
<body>

<section class="card card--front" aria-label="Card front">
  <svg class="card__art" width="700" height="400" viewBox="0 0 700 400">
    <rect width="700" height="400" fill="var(--card-grey)"/>
    <polygon points="0,0 260,0 0,170" fill="var(--grey-light)" opacity="0.5"/>
    <polygon points="700,0 430,0 700,230" fill="var(--grey-mid)" opacity="0.6"/>
    <polygon points="0,400 0,260 200,400" fill="var(--grey-mid)" opacity="0.6"/>
    <polygon points="700,400 520,400 700,300" fill="var(--grey-light)" opacity="0.45"/>
  </svg>
  <div class="wordmark"><span class="wordmark__dot"></span>K&amp;R</div>
</section>

<section class="card card--back" aria-label="Card back">
  <svg class="card__art" width="700" height="400" viewBox="0 0 700 400">
    <rect width="700" height="400" fill="var(--card-grey)"/>
    <polygon points="0,0 170,0 0,120" fill="var(--grey-light)" opacity="0.45"/>
    <path d="M0,200 C220,190 470,110 700,30 L700,400 L0,400 Z" fill="var(--grey-light)"/>
    <path d="M0,215 C230,205 480,135 700,65 L700,400 L0,400 Z" fill="var(--grey-deep)"/>
    <path d="M0,230 C240,220 490,160 700,100 L700,400 L0,400 Z" fill="var(--band-dark)"/>
    <rect x="0" y="345" width="700" height="55" fill="var(--card-grey)"/>
    <polygon points="0,345 700,345 700,352 0,352" fill="var(--grey-light)"/>
  </svg>

  <div class="wordmark"><span class="wordmark__dot"></span>K&amp;R</div>

  <div class="person">
    <div class="person__name">Owen Calder</div>
    <div class="person__title">Executive Director</div>
  </div>

  <div class="contact">
    <div class="contact__company">K&amp;R SECURITY SERVICES PTY. LTD.</div>
    <div class="contact__address">218 Harlow St, Brenton NSW 2790</div>
    <div class="contact__row">
      <svg class="contact__icon" viewBox="0 0 14 14"><path d="M1,5 Q7,0 13,5 L11,7 9,5 5,5 3,7 Z M3,8 h8 v4 h-8 Z" fill="var(--text-light)"/></svg>
      <span>(02) 6000 1284</span>
    </div>
    <div class="contact__row">
      <svg class="contact__icon" viewBox="0 0 14 14"><rect x="1" y="3" width="12" height="8" fill="var(--text-light)"/><path d="M1,3 L7,8 L13,3" stroke="var(--band-dark)" stroke-width="1.3" fill="none"/></svg>
      <span>admin@k&amp;rsecurity.com</span>
    </div>
    <div class="contact__row">
      <svg class="contact__icon" viewBox="0 0 14 14"><rect x="1" y="6" width="7" height="4" rx="2" transform="rotate(-45 4.5 8)" stroke="var(--text-light)" stroke-width="1.4" fill="none"/><rect x="6" y="4" width="7" height="4" rx="2" transform="rotate(-45 9.5 6)" stroke="var(--text-light)" stroke-width="1.4" fill="none"/></svg>
      <span>k&amp;rsecurity.com</span>
    </div>
  </div>
</section>

</body>
</html>
```